Wordpress Design Project

I would like a Quarto-based Wordpress design for my site - BondKestrel.com. The purpose of this site is to build a community that follow along on my journey from $0 to $100,000 in trading profits. The goal of the home page is to capture the viewer's email address. There will be a feature box with video of me and an opt-in to the right. I purchased a skin that I'm not happy with it, but you can get an idea of what I was trying to do by visiting the site now. You'll see that I already have the logo. The second most important thing to me is ease of navigation. There should be a prominent navigation bar underneath the feature box. See the nav bar at quietmeadowfunds.com for an example. I'll be following a similar content strategy with a lot of educational posts and a separate page for podcasts and videos.
Updates
I just updated the brief to be more specific about the page elements and features I'm looking for. Hopefully this will answer most of the questions I've received so far.
Project Deadline Extended
Reason: I'm extending the deadline because I'll be on vacation for about 5 days and I want to make sure I have enough time to provide feedback and evaluate the designs. Thanks for everyone who has submitted so far - the designs look good.
Requirements
Must have
- The front page will be the blog with the following from top to bottom:
1) BondKestrel logo
2) Video and large email signup form (no name, just email address). I use Mailorix for my email list if that makes a difference.
3) Navigation bar
All other pages will not have item 2 above, but should have an email signup form in the right side bar.
Right side bar functionality should mimic quietmeadowfunds.com to include:
1) Email signup form
2) Multi-tab post menu that I can edit
3) Search box
4) Place to list foundation content links

```html
<!DOCTYPE html>
<html lang="en">
<head>
<meta charset="utf-8">
<title>BondKestrel — Home</title>
<link rel="stylesheet" href="https://fonts.googleapis.com/css2?family=Ubuntu:wght@400;500&family=PT+Sans:wght@400;700&family=Gelasio:wght@400&display=swap">
<style>
:root{
  --band:#e8e7e8;
  --white:#ffffff;
  --ink:#333333;
  --body:#555555;
  --muted:#8a8a8a;
  --green:#2f7d10;
  --green-bright:#4aa51c;
  --green-pale:#b7d77a;
  --red:#7e0c0c;
  --field:#6b6b6b;
  --nav-top:#4a4a4a;
  --nav-bottom:#0e0e0e;
  --footer:#1f1f1f;
  --footer-text:#bdbdbd;
  --date:#e4a11b;
  --social-blue:#3b5998;
}
*{box-sizing:border-box;margin:0;padding:0}
html,body{width:776px;height:1200px;overflow:hidden;background:var(--white)}
body{position:relative;font-family:"PT Sans",Arial,sans-serif;color:var(--ink)}
.abs{position:absolute}
.top-band{left:0;top:0;width:776px;height:165px;background:var(--band)}

/* header */
.brand{left:90px;top:12px;display:flex;align-items:center;gap:10px}
.brand-mark{width:50px;height:50px;border-radius:50%;background:#1c1c1c}
.brand-name{font-family:"Ubuntu",sans-serif;font-size:33px;font-weight:400;color:var(--green);letter-spacing:-0.5px}
.signup-label{left:398px;top:10px;font-family:"Ubuntu",sans-serif;font-size:14px;color:#222}
.social-dot{top:10px;width:17px;height:17px;border-radius:50%;border:1px solid #9a9a9a;background:#e2e2e2}
.field{background:#fff;border:1px solid #d0d0d0;border-radius:3px;font-size:9px;color:#666;padding:6px 8px}
.btn-signup{left:626px;top:38px;width:47px;height:24px;background:var(--red);border-radius:3px;color:#fff;font-size:9px;font-weight:700;display:flex;align-items:center;justify-content:center}

/* feature video */
.video-frame{left:97px;top:84px;width:377px;height:240px;border:1px solid #b8b8b8;border-radius:5px;background:#f4f4f4;box-shadow:0 1px 3px rgba(0,0,0,.15)}
.video-still{left:104px;top:90px;width:363px;height:210px;background:linear-gradient(90deg,#f1f3f5 0%,#dbe6ee 45%,#c9d9e5 100%)}
.play-ring{left:258px;top:168px;width:54px;height:54px;border-radius:50%;border:4px solid rgba(255,255,255,.85)}
.player-bar{left:104px;top:300px;width:363px;height:17px;background:linear-gradient(#e9e9e9,#c9c9c9);border-top:1px solid #aaa}
.player-time{left:385px;top:303px;font-size:7px;color:#333}

/* newsletter */
.newsletter{left:497px;top:84px;width:182px;height:240px;border:1px solid #c6c6c6;border-radius:5px;background:linear-gradient(#f7f7f7,#e6e6e6)}
.newsletter-head{left:498px;top:85px;width:180px;height:31px;background:linear-gradient(#5fb12a,#38900f);border-radius:4px 4px 0 0;color:#fff;font-family:"Ubuntu",sans-serif;font-size:19px;padding:3px 0 0 14px}
.newsletter-copy{left:514px;top:127px;width:150px;font-size:8.4px;line-height:13.6px;color:#555}
.nl-label{left:516px;font-size:10px;color:#222}
.nl-field{left:515px;width:146px;height:20px;background:var(--field);border:1px solid #555;border-radius:2px}
.btn-subscribe{left:517px;top:285px;width:142px;height:23px;background:linear-gradient(#c9e396,#a4c965);border:1px solid #8fb35a;border-radius:3px;font-family:"Ubuntu",sans-serif;font-size:14px;color:#2b3a12;letter-spacing:.5px;display:flex;align-items:center;justify-content:center}

/* navigation */
.main-nav{left:0;top:345px;width:776px;height:46px;background:linear-gradient(var(--nav-top),var(--nav-bottom))}
.nav-item{top:345px;height:46px;padding-top:13px;font-family:"Ubuntu",sans-serif;color:#bdbdbd}
.nav-item b{display:block;font-weight:400;font-size:10px;line-height:11px}
.nav-item span{display:block;font-size:7.5px;line-height:10px;color:#9a9a9a}
.nav-item.is-active{background:var(--green-bright);color:#fff;padding-left:8px;width:61px}
.nav-item.is-active span{color:#eaf7e0}

/* posts */
.page-title{left:91px;top:416px;width:370px;font-family:"Ubuntu",sans-serif;font-size:17.5px;line-height:20px;color:var(--green)}
.post-thumb{left:91px}
.post-title{left:170px;font-family:"Gelasio",Georgia,serif;font-size:11px;color:#222}
.post-text{left:170px;width:298px;font-size:8.4px;line-height:13.1px;color:var(--body)}
.divider{left:91px;width:376px;height:6px;background:repeating-linear-gradient(90deg,#d4d4d4 0 1px,transparent 1px 3px)}
.divider::after{content:"";position:absolute;left:172px;top:0;width:30px;height:6px;background:repeating-linear-gradient(90deg,#555 0 1px,transparent 1px 3px)}
.content-edge{left:476px;top:395px;width:10px;height:575px;background:linear-gradient(90deg,rgba(0,0,0,.07),rgba(0,0,0,0))}

/* sidebar */
.side-head{left:542px;font-family:"Ubuntu",sans-serif;font-size:14px;line-height:14px;color:var(--green)}
.side-head small{display:block;font-size:11.5px;line-height:14px;color:#8a8a8a}
.side-field{left:503px;height:21px;border:1px solid #c6c6c6;border-radius:10px;background:#fff;font-size:8px;color:#666;padding:5px 8px}
.btn-search{left:643px;top:466px;width:24px;height:21px;background:#555;border-radius:0 10px 10px 0}
.btn-join{left:503px;top:602px;width:101px;height:20px;background:linear-gradient(#6a6a6a,#2e2e2e);border-radius:10px;color:#fff;font-size:8.5px;display:flex;align-items:center;justify-content:center}
.side-rule{left:503px;width:182px;height:1px;background:#e2e2e2}

/* footer */
.site-footer{left:0;top:990px;width:776px;height:210px;background:var(--footer)}
.foot-head{top:1011px;font-family:"Ubuntu",sans-serif;font-size:9.5px;font-weight:500;color:#fff;letter-spacing:.3px}
.foot-list{top:1028px;font-size:8.3px;line-height:11px;color:var(--footer-text);list-style:none}
.news-item{left:374px;font-size:8px;line-height:11px;color:var(--footer-text)}
.news-item em{font-style:normal;color:var(--date);display:block}
.social-widget{left:527px;top:1011px;width:158px;height:148px;background:#fff;border:1px solid #bbb}
.foot-rule{left:0;top:1171px;width:776px;height:1px;background:#333}
.copyright{left:91px;top:1184px;font-size:7px;color:#8a8a8a}
.foot-square{top:1179px;width:10px;height:10px;background:#4a6ea8;border-radius:1px}

/* widget internals */
.w-text{font-size:7px;color:#333}
.avatar{width:24px;height:24px}
.avatar-name{font-size:6.5px;color:#333}
</style>
</head>
<body>

<div class="abs top-band"></div>

<header>
  <div class="abs brand"><div class="brand-mark"></div><div class="brand-name">BondKestrel</div></div>
  <div class="abs signup-label">Sign Up</div>
  <div class="abs social-dot" style="left:611px"></div>
  <div class="abs social-dot" style="left:632px"></div>
  <div class="abs social-dot" style="left:653px"></div>
  <div class="abs field" style="left:397px;top:38px;width:111px;height:24px">Name</div>
  <div class="abs field" style="left:511px;top:38px;width:111px;height:24px">Email</div>
  <div class="abs btn-signup">Sign Up</div>
</header>

<section class="feature">
  <div class="abs video-frame"></div>
  <div class="abs video-still" role="img" aria-label="Video still of the host presenting in front of a pale blue trading chart"></div>
  <div class="abs play-ring"></div>
  <svg class="abs" style="left:278px;top:184px" width="20" height="22" viewBox="0 0 20 22"><path d="M2 1 L19 11 L2 21 Z" fill="rgba(255,255,255,.85)"/></svg>
  <div class="abs player-bar"></div>
  <svg class="abs" style="left:104px;top:300px" width="363" height="17" viewBox="0 0 363 17">
    <path d="M6 4 L14 8.5 L6 13 Z" fill="#333"/>
    <line x1="20" y1="0" x2="20" y2="17" stroke="#999"/>
    <rect x="26" y="6" width="244" height="5" rx="2.5" fill="#9a9a9a"/>
    <circle cx="29" cy="8.5" r="4" fill="#555"/>
    <line x1="320" y1="0" x2="320" y2="17" stroke="#999"/>
    <path d="M325 6 h3 l4 -3 v11 l-4 -3 h-3 Z" fill="#333"/>
    <rect x="346" y="4" width="12" height="9" fill="#555"/>
  </svg>
  <div class="abs player-time">0:00 / 0:00</div>

  <aside class="abs newsletter"></aside>
  <div class="abs newsletter-head">Our Newsletter!</div>
  <p class="abs newsletter-copy">Lorem ipsum dolor sit amet, consectetur adipisicing elit, sed do eiusmod tempor incididunt ut labore et dolore magna aliqua.</p>
  <div class="abs nl-label" style="top:192px">First Name</div>
  <div class="abs nl-field" style="top:207px"></div>
  <div class="abs nl-label" style="top:233px">Email</div>
  <div class="abs nl-field" style="top:248px"></div>
  <div class="abs btn-subscribe">SUBSCRIBE</div>
</section>

<nav>
  <div class="abs main-nav"></div>
  <div class="abs nav-item is-active" style="left:91px"><b>Home</b><span>Back to Start</span></div>
  <div class="abs nav-item" style="left:162px"><b>About</b><span>Who is Rowan?</span></div>
  <div class="abs nav-item" style="left:220px"><b>Archives</b><span>Hall of Records</span></div>
  <div class="abs nav-item" style="left:290px"><b>Podcast</b><span>Tunebay Broadcast</span></div>
  <div class="abs nav-item" style="left:366px"><b>Videos</b><span>How To Vids</span></div>
  <div class="abs nav-item" style="left:425px"><b>Income Reports</b><span>How I Make a Living Online</span></div>
  <div class="abs nav-item" style="left:537px"><b>Resources</b><span>Tools of the Trade</span></div>
  <div class="abs nav-item" style="left:616px"><b>Contact</b><span>Get a Hold of Me</span></div>
</nav>

<main>
  <h1 class="abs page-title" style="font-weight:400">Creating Financial Independence Through Stupid Simple Options Trading</h1>

  <div class="abs post-thumb" style="top:479px;width:54px;height:66px;background:linear-gradient(#2a4a8a 0 22%,#f2c81a 22% 100%)" role="img" aria-label="Cover of a beginner options trading book"></div>
  <h2 class="abs post-title" style="top:480px;font-weight:400">By Beginner, For Beginner</h2>
  <p class="abs post-text" style="top:494px">I've sampled a butt-load of Options Trading education by "25 year veterans" and I've been consistently frustrated by their inability to remember what it was like before they understood any of this stuff. They constantly talk over your head and refer to terms and concepts that haven't been explained yet. It makes the learning process REALLY frustrating. In my career as a management consultant, I'm often charged with learning new subject matter and developing simple, incisive training media and I'm pretty darn good at it. I know teaching you will help me master Options Trading because beginners ask the best questions. You benefit because I'll always be a few steps ahead of you doing what I do best - stripping out the fluff and passing only the essential knowledge you need to succeed.</p>
  <div class="abs divider" style="top:648px"></div>

  <div class="abs post-thumb" style="top:679px;width:64px;height:43px;background:#24303e" role="img" aria-label="Dark slate card with a keep it simple slogan"></div>
  <div class="abs" style="left:91px;top:722px;width:64px;height:14px;background:linear-gradient(rgba(36,48,62,.25),rgba(36,48,62,0))"></div>
  <h2 class="abs post-title" style="top:678px;font-weight:400">Stupid Simple</h2>
  <p class="abs post-text" style="top:692px">Options Trading can be REALLY complicated. There are a bazillion strategies, complex trading software, and the unpredictable nature of the stock market all conspiring to make you broke. I break it down. We take things one by one. Terminology, foundational concepts, and demonstrations are all structured to build your knowledge and expertise over time for deeper understanding.</p>
  <div class="abs divider" style="top:781px"></div>

  <div class="abs post-thumb" style="top:811px;width:64px;height:95px;background:linear-gradient(160deg,#7a5a44,#c89478 55%,#3a2a22)" role="img" aria-label="Portrait photo of the author"></div>
  <div class="abs" style="left:91px;top:906px;width:64px;height:14px;background:linear-gradient(rgba(90,60,45,.2),rgba(90,60,45,0))"></div>
  <h2 class="abs post-title" style="top:810px;font-weight:400">Insane Quality</h2>
  <p class="abs post-text" style="top:824px">I'm kind of obsessed with this stuff. I don't sleep. I don't eat. I stare at stock charts until my eyes bleed. To complement this unhealthy dedication to the subject matter, I'm a bit of a quality freak. I'm the kind of guy that reads emails 3 times before I send them to check for typos and make sure the content flows well. I hope you appreciate my insanity.</p>

  <div class="abs content-edge"></div>
</main>

<aside class="sidebar">
  <svg class="abs" style="left:503px;top:420px" width="30" height="30" viewBox="0 0 30 30">
    <circle cx="11" cy="11" r="8" fill="#dbe9f5" stroke="#8aa4bb" stroke-width="2.5"/>
    <line x1="17" y1="17" x2="27" y2="27" stroke="#6b6b6b" stroke-width="4" stroke-linecap="round"/>
  </svg>
  <div class="abs side-head" style="top:424px">Quick Search<small>For BondKestrel</small></div>
  <div class="abs side-field" style="top:466px;width:141px;border-radius:10px 0 0 10px">Search...</div>
  <div class="abs btn-search"></div>
  <svg class="abs" style="left:649px;top:470px" width="13" height="13" viewBox="0 0 13 13"><circle cx="5.5" cy="5.5" r="3.8" fill="none" stroke="#fff" stroke-width="1.6"/><line x1="8.3" y1="8.3" x2="12" y2="12" stroke="#fff" stroke-width="1.8"/></svg>
  <div class="abs side-rule" style="top:506px"></div>

  <svg class="abs" style="left:503px;top:522px" width="32" height="34" viewBox="0 0 32 34">
    <circle cx="16" cy="10" r="7" fill="#c98a4a"/>
    <path d="M3 33 C3 22 9 18 16 18 C23 18 29 22 29 33 Z" fill="#4a9ad4"/>
  </svg>
  <div class="abs side-head" style="top:530px">Free Membership<small>For BondKestrel</small></div>
  <div class="abs side-field" style="top:570px;width:164px">Email...</div>
  <div class="abs btn-join">Join The Revolution</div>
  <div class="abs side-rule" style="top:640px"></div>
</aside>

<footer>
  <div class="abs site-footer"></div>

  <div class="abs foot-head" style="left:91px">QUICK LINKS</div>
  <ul class="abs foot-list" style="left:91px">
    <li>Home</li><li>About</li><li>Archives</li><li>Podcast</li><li>Vidoe</li><li>Income Reports</li><li>Resources</li><li>Contact</li>
  </ul>

  <div class="abs foot-head" style="left:210px">CONTACT US</div>
  <ul class="abs foot-list" style="left:213px">
    <li>012 Lorem Ipsum,</li><li>dummy text.</li><li>(000) 123-4567 Phone</li><li>(000) 123-4567 Fax</li>
    <li style="color:#fff;margin-top:4px">Email-info@bondkestrel.com</li>
  </ul>

  <div class="abs foot-head" style="left:374px">LATEST NEWS</div>
  <div class="abs news-item" style="top:1030px"><em>12 March, 2012</em>Lorem Ipsum is simply dummy text...</div>
  <div class="abs news-item" style="top:1063px"><em>12 March, 2012</em>Lorem Ipsum is simply dummy text...</div>
  <div class="abs news-item" style="top:1096px"><em>12 March, 2012</em>Lorem Ipsum is simply dummy text...</div>

  <div class="abs social-widget">
    <div class="abs" style="left:8px;top:8px;width:20px;height:20px;border-radius:50%;background:#1c1c1c"></div>
    <div class="abs w-text" style="left:42px;top:7px;color:var(--social-blue)"><b>BondKestrel</b> on Circlefeed</div>
    <div class="abs w-text" style="left:36px;top:19px;width:28px;height:13px;border:1px solid #9aa;border-radius:2px;background:#eef;padding:1px 6px;color:var(--social-blue)">Like</div>
    <div class="abs" style="left:113px;top:17px;width:37px;height:15px;background:#5aa02c;border:1px solid #3f7a1c;color:#fff;font-size:7.5px;font-weight:700;display:flex;align-items:center;justify-content:center">Sign Up</div>
    <div class="abs w-text" style="left:6px;top:41px;font-size:6.5px">560 people like <b>BondKestrel</b></div>

    <div class="abs avatar" style="left:7px;top:54px;background:#d6a08c" role="img" aria-label="Member photo"></div>
    <div class="abs avatar" style="left:40px;top:54px;background:#8fa2b8" role="img" aria-label="Member photo"></div>
    <div class="abs avatar" style="left:73px;top:54px;background:#a07860" role="img" aria-label="Member photo"></div>
    <div class="abs avatar" style="left:106px;top:54px;background:#9a8f88" role="img" aria-label="Member photo"></div>
    <div class="abs avatar-name" style="left:6px;top:80px">Stacey</div>
    <div class="abs avatar-name" style="left:40px;top:80px">Murry</div>
    <div class="abs avatar-name" style="left:71px;top:80px">Amanda</div>
    <div class="abs avatar-name" style="left:106px;top:80px">Marie</div>

    <div class="abs avatar" style="left:7px;top:95px;background:#c88f7a" role="img" aria-label="Member photo"></div>
    <div class="abs avatar" style="left:40px;top:95px;background:#7a8a6a" role="img" aria-label="Member photo"></div>
    <div class="abs avatar" style="left:73px;top:95px;background:#8a6a8a" role="img" aria-label="Member photo"></div>
    <div class="abs avatar" style="left:106px;top:95px;background:#b0806a" role="img" aria-label="Member photo"></div>
    <div class="abs avatar-name" style="left:6px;top:121px">Lisa</div>
    <div class="abs avatar-name" style="left:40px;top:121px">Brett</div>
    <div class="abs avatar-name" style="left:71px;top:121px">Rebecca</div>
    <div class="abs avatar-name" style="left:106px;top:121px">Zane</div>

    <div class="abs" style="left:4px;top:133px;width:148px;height:1px;background:#ddd"></div>
    <div class="abs" style="left:5px;top:136px;width:8px;height:8px;background:var(--social-blue)"></div>
    <div class="abs w-text" style="left:16px;top:135px;font-size:6px;color:#666">Circlefeed social plugin</div>
  </div>

  <div class="abs foot-rule"></div>
  <div class="abs copyright">© 2012 BondKestrel.  All Rights Reserved.</div>
  <div class="abs foot-square" style="left:641px"></div>
  <div class="abs foot-square" style="left:658px"></div>
  <div class="abs foot-square" style="left:675px"></div>
</footer>

</body>
</html>
```